Brightpath, LLC
Electrical Contracting Company
We really like the back of #125 & #126 and the logo design on the front of #125.
We liked the front layout of #122, and we especially liked how they included the phrase Electrical Contracting Company on the card.
#118 we really like the front and back of your card. We like the colors, we like the shadowing.
We like the symbols for phone, cell, etc.
The above info was updated in the brief summary.
Please not changes to information:
instead of Electrical Contracting Corporation it needs to be Electrical Contracting Company
And the Fax number is 612-437-2908

```html
<!DOCTYPE html>
<html lang="en">
<head>
<meta charset="utf-8">
<title>Brightpath, LLC — Business Card</title>
<link href="https://fonts.googleapis.com/css2?family=Open+Sans:wght@400;600&display=swap" rel="stylesheet">
<style>
  :root {
    --stage: #3a3a3a;
    --card-dark: #1c1c1d;
    --card-mid: #2a2a2b;
    --brand-red: #c4201f;
    --band: #4a4a4b;
    --text-light: #e6e6e6;
    --text-muted: #b3b3b3;
    --mark-faint: #3b3b3c;
  }
  * { margin: 0; padding: 0; box-sizing: border-box; }
  html, body { width: 1200px; height: 799px; overflow: hidden; }
  body {
    background: var(--stage);
    font-family: "Open Sans", Arial, sans-serif;
    position: relative;
  }
  .card {
    position: absolute;
    width: 520px;
    height: 298px;
    border-radius: 14px;
    background: linear-gradient(160deg, var(--card-mid) 0%, var(--card-dark) 70%);
    box-shadow: 0 14px 30px rgba(0,0,0,.45);
    overflow: hidden;
  }
  .card-front { left: 50px; top: 250px; }
  .card-back { left: 630px; top: 250px; }

  /* Front */
  .brand-block {
    position: absolute;
    left: 34px; top: 60px;
    width: 150px; height: 150px;
    background: var(--brand-red);
    display: flex; align-items: center; justify-content: center;
  }
  .brand-square {
    width: 46px; height: 46px;
    background: var(--card-dark);
  }
  .brand-name {
    position: absolute;
    left: 34px; top: 214px;
    width: 150px;
    text-align: center;
    font-size: 14px;
    font-weight: 600;
    color: var(--text-light);
    letter-spacing: .5px;
  }
  .service-band {
    position: absolute;
    left: 34px; right: 0; top: 244px;
    height: 20px;
    background: var(--band);
    display: flex; align-items: center;
    padding-left: 14px;
    font-size: 9.5px;
    letter-spacing: 1px;
    color: var(--text-light);
    text-transform: uppercase;
  }
  .person {
    position: absolute;
    right: 34px; top: 22px;
    text-align: right;
  }
  .person-name { color: var(--brand-red); font-size: 22px; font-weight: 600; line-height: 1.1; }
  .person-title { color: var(--text-light); font-size: 12px; }
  .address {
    position: absolute;
    right: 34px; top: 80px;
    text-align: right;
    font-size: 11px;
    line-height: 1.4;
    color: var(--text-light);
  }
  .contact {
    position: absolute;
    right: 34px; top: 128px;
    display: flex; gap: 6px; align-items: flex-start;
  }
  .contact-lines {
    text-align: right;
    font-size: 11px;
    line-height: 1.55;
    color: var(--text-light);
  }
  .contact-labels {
    writing-mode: vertical-rl;
    transform: rotate(180deg);
    font-size: 9px;
    font-weight: 600;
    color: var(--brand-red);
    letter-spacing: 1px;
    text-transform: uppercase;
  }

  /* Back */
  .back-mark {
    position: absolute;
    left: 40px; top: 100px;
    font-size: 44px;
    font-weight: 600;
    color: var(--mark-faint);
  }
  .back-url {
    position: absolute;
    right: 30px; bottom: 22px;
    font-size: 11px;
    color: var(--text-muted);
  }
</style>
</head>
<body>
  <section class="card card-front">
    <div class="brand-block"><div class="brand-square"></div></div>
    <div class="brand-name">Brightpath, LLC</div>
    <div class="service-band">Electrical Contracting Company</div>

    <div class="person">
      <div class="person-name">Dana Whitcomb</div>
      <div class="person-title">President</div>
    </div>

    <div class="address">48 Ridgeline Rd. &nbsp;Fairhaven<br>NY 12345</div>

    <div class="contact">
      <div class="contact-lines">
        6124370815<br>
        6129126643<br>
        612-437-2908<br>
        dana@brightpathllc.com
      </div>
      <div class="contact-labels">office · cell · fax</div>
    </div>
  </section>

  <section class="card card-back">
    <div class="back-mark">Brightpath, LLC</div>
    <div class="back-url">www.brightpathllc.com</div>
  </section>
</body>
</html>
```